Powepoint Templates From Logo

Hello,

I am looking for a template for PowerPoint presentations for a new company selling LED's. The PowerPoint should keep the look and feel of our newly designed website ( which is still under development ) http://brivonlux.com/development/

I have attached our Logo which should be included in this template.
This PowerPoint will be used towards client during demonstrations and for internal use.

This template should be complete with fonts and colors of the text for both headlines and bullets/normal text.

I guess the easiest way for me to determine what I like is to see some dummy info/text on the submitted designs.

Thanks

Industry/Entity Type

It Company

Requirements
Must have
• Should include our logo

```html
<!DOCTYPE html>
<html lang="en">
<head>
<meta charset="utf-8">
<title>Brivonlux Presentation Template</title>
<link href="https://fonts.googleapis.com/css2?family=Arimo:wght@400;700&display=swap" rel="stylesheet">
<style>
:root{
  --green:#8cc63f;
  --green-light:#c8e840;
  --green-dark:#6aae1f;
  --grey-text:#333333;
  --grey-soft:#9a9a9a;
  --grey-band:#e3e3e3;
  --slide-top:#e9eaec;
  --frame:#8a8a8a;
  --white:#ffffff;
}
*{margin:0;padding:0;box-sizing:border-box}
html,body{width:1200px;height:1020px;overflow:hidden;background:var(--white)}
body{position:relative;font-family:"Arimo",Arial,sans-serif}
.slide{position:absolute;width:578px;height:379px;border:1px solid var(--frame);overflow:hidden;
  background:linear-gradient(180deg,var(--slide-top) 0%,var(--white) 45%,var(--white) 100%)}
.slide--cover{left:14px;top:115px}
.slide--why{left:599px;top:115px}
.slide--bulbs{left:14px;top:502px}
.slide--advantage{left:599px;top:502px}
.footer{position:absolute;left:0;right:0;bottom:0;height:36px;background:var(--grey-band);
  font-size:12px;font-weight:700;letter-spacing:2px;color:var(--green);line-height:36px;text-align:right;padding-right:30px}
.slide--cover .footer{text-align:center;padding:0;color:#555;background:linear-gradient(180deg,#f1f1f1,#e6e6e6)}
.rule{position:absolute;left:0;right:0;height:3px;background:linear-gradient(90deg,var(--green-light),var(--green),var(--green-light))}
.lamp-area{position:absolute;left:262px;top:0;width:66px;height:112px;background:linear-gradient(180deg,#e4e4e4,#f4f4f4)}
.cover-brand{position:absolute;left:0;right:0;top:178px;text-align:center}
.brand{display:inline-flex;align-items:center;gap:10px;font-weight:700;color:#6d6d6d}
.brand__dot{display:inline-block;border-radius:50%;background:var(--green)}
.cover-brand .brand{font-size:46px}
.cover-brand .brand__dot{width:54px;height:54px}
.cover-shadow{position:absolute;left:180px;top:262px;width:220px;height:14px;border-radius:50%;
  background:radial-gradient(ellipse,rgba(0,0,0,.16),rgba(0,0,0,0) 70%)}
.corner-brand{position:absolute;right:26px;top:22px}
.corner-brand .brand{font-size:22px;gap:6px}
.corner-brand .brand__dot{width:28px;height:28px}
.title-tab{position:absolute;left:0;top:31px;height:42px;padding:0 24px 0 20px;border-radius:0 21px 21px 0;
  background:linear-gradient(180deg,var(--green-light),var(--green) 60%,var(--green-dark));
  color:var(--white);font-size:25px;font-weight:400;line-height:42px;letter-spacing:-.5px;white-space:nowrap}
.title-tab b{font-weight:700}
.body-text{position:absolute;color:var(--grey-text);font-weight:700;text-align:justify}
.slide--why .body-text{left:155px;top:93px;width:394px;font-size:14px;line-height:18px}
.slide--advantage .body-text{left:264px;top:101px;width:284px;font-size:11px;line-height:14.4px}
.product-grid{position:absolute;left:163px;top:90px;display:grid;grid-template-columns:repeat(4,91px);grid-auto-rows:78px;gap:9px 7px}
.product-tile{border:2px solid var(--green)}
.tile-a{background:#a9afbf}
.tile-b{background:#3f6fa8}
.tile-c{background:#6a2a62}
.tile-d{background:#958a72}
.tile-e{background:#a8707a}
.tile-f{background:#c7b093}
.tile-g{background:#8f8470}
.tile-h{background:#ececec}
.products-label{position:absolute;left:163px;top:282px;font-size:33px;font-weight:700;color:var(--grey-soft);letter-spacing:-.5px}
.advantage-photo{position:absolute;left:29px;top:125px;width:215px;height:143px;border:2px solid var(--green);
  background:linear-gradient(135deg,#b8d0e0,#a7c486)}
</style>
</head>
<body>
  <section class="slide slide--cover">
    <div class="lamp-area" role="img" aria-label="White LED light bulb hanging from the top edge"></div>
    <div class="rule" style="top:70px"></div>
    <div class="cover-brand"><span class="brand"><span class="brand__dot"></span>Brivonlux</span></div>
    <div class="cover-shadow"></div>
    <div class="rule" style="top:340px"></div>
    <div class="footer">www.brivonlux.com</div>
  </section>

  <section class="slide slide--why">
    <h2 class="title-tab">Why <b>LED?</b></h2>
    <div class="corner-brand"><span class="brand"><span class="brand__dot"></span>Brivonlux</span></div>
    <p class="body-text">It is a long established fact that a reader will be distracted by the readable content of a page when looking at its layout. The point of using Lorem Ipsum is that it has a more-or-less normal distribution of letters, as opposed to using ‘Content here, content here’, making it look like readable English. Many desktop publishing packages and web page editors now use Lorem Ipsum as their default model text, and a search for ‘lorem ipsum’ will uncover many web sites still in their infancy. Various versions have evolved over the years, sometimes by accident, sometimes on purpose (injected humour and the like).</p>
    <div class="footer">www.brivonlux.com</div>
  </section>

  <section class="slide slide--bulbs">
    <h2 class="title-tab"><b>LED</b> Bulb</h2>
    <div class="corner-brand"><span class="brand"><span class="brand__dot"></span>Brivonlux</span></div>
    <div class="product-grid">
      <div class="product-tile tile-a" role="img" aria-label="Coloured candle-shaped bulbs"></div>
      <div class="product-tile tile-b" role="img" aria-label="Glowing round LED light"></div>
      <div class="product-tile tile-c" role="img" aria-label="Pink spotlight beam"></div>
      <div class="product-tile tile-d" role="img" aria-label="Row of LED bulbs"></div>
      <div class="product-tile tile-e" role="img" aria-label="Rows of multicoloured small bulbs"></div>
      <div class="product-tile tile-f" role="img" aria-label="Lamp socket component"></div>
      <div class="product-tile tile-g" role="img" aria-label="Ceramic bulb holder"></div>
      <div class="product-tile tile-h" role="img" aria-label="White LED bulb"></div>
    </div>
    <p class="products-label">All Products</p>
    <div class="footer">www.brivonlux.com</div>
  </section>

  <section class="slide slide--advantage">
    <h2 class="title-tab">Advantage of <b>LED</b></h2>
    <div class="corner-brand"><span class="brand"><span class="brand__dot"></span>Brivonlux</span></div>
    <div class="advantage-photo" role="img" aria-label="Hands holding a small tree against a sky and grass"></div>
    <p class="body-text">It is a long established fact that a reader will be distracted by the readable content of a page when looking at its layout. The point of using Lorem Ipsum is that it has a more-or-less normal distribution of letters, as opposed to using ‘Content here, content here’, making it look like readable English. Many desktop publishing packages and web page editors now use Lorem Ipsum as their default model text, and a search for ‘lorem ipsum’ will uncover many web sites still in their infancy. Various versions have evolved over the years, sometimes by accident, sometimes on purpose (injected humour and the like).</p>
    <div class="footer">www.brivonlux.com</div>
  </section>
</body>
</html>
```